TRY-THE-LANTERN Business Card Design

Please do not submit more than one design per designer. Both the front and the back must be submitted as a single design. Please use all of the attached files to design a two-sided business card. Do not use tiny text that is hard to read. Do not put text or images too close to the edges where it might get cut off during printing. The card should be horizontal. Please do not send me the same design that I attached showing the business information. Be creative.

One file is marked as the primary logo for company. Other files are marked as secondary. All logos should be incorporated into the design with a focus on the primary one being bigger.

```html
<!DOCTYPE html>
<html lang="en">
<head>
<meta charset="utf-8">
<title>TRY-THE-LANTERN Business Card</title>
<link rel="stylesheet" href="https://fonts.googleapis.com/css2?family=Saira:ital,wght@0,800;1,800&family=Lexend:wght@300;400&display=swap">
<style>
  :root {
    --backdrop: #2a8a8c;
    --card-light: #ffffff;
    --card-dark: #000000;
    --ink: #111111;
    --paper-text: #ffffff;
    --badge-ring: #111111;
    --badge-fill: #d9dde6;
    --art-top: #f2f2f2;
    --art-bottom: #5a5a5a;
  }
  * { box-sizing: border-box; margin: 0; padding: 0; }
  html, body { width: 1200px; height: 1000px; overflow: hidden; }
  body { background: var(--backdrop); position: relative; font-family: "Lexend", sans-serif; }

  .card { position: absolute; }
  .card-front {
    left: 302px; top: 130px; width: 593px; height: 338px;
    background: var(--card-light); color: var(--ink);
  }
  .card-back {
    left: 280px; top: 533px; width: 615px; height: 338px;
    background: var(--card-dark); color: var(--paper-text);
  }

  .holder-name {
    position: absolute; left: 29px; top: 36px;
    font-family: "Saira", sans-serif; font-style: italic; font-weight: 800;
    font-size: 21px; letter-spacing: 1.2px; text-transform: uppercase; white-space: nowrap;
  }
  .credentials {
    position: absolute; left: 29px; top: 72px;
    list-style: none; font-size: 19px; line-height: 27px; font-weight: 300;
  }
  .divider {
    position: absolute; left: 29px; top: 193px; width: 388px; height: 2px; background: var(--ink);
  }
  .contacts { position: absolute; left: 29px; top: 212px; list-style: none; }
  .contacts li {
    display: flex; align-items: center; gap: 12px;
    font-size: 19px; font-weight: 300; height: 28px; margin-bottom: 11px; white-space: nowrap;
  }
  .contacts svg { width: 13px; height: 13px; flex: none; }

  .badges { position: absolute; left: 492px; top: 30px; list-style: none; }
  .badges li {
    width: 63px; height: 63px; border-radius: 50%;
    border: 3px solid var(--badge-ring); background: var(--card-light);
    display: flex; align-items: center; justify-content: center;
    margin-bottom: 9px;
  }
  .badges li span { width: 49px; height: 49px; border-radius: 50%; background: var(--badge-fill); }

  .boat-art {
    position: absolute; left: 198px; top: 76px; width: 210px; height: 84px;
    border-radius: 30% 60% 45% 20% / 40% 60% 40% 40%;
    background: linear-gradient(180deg, var(--art-top), var(--art-bottom));
    opacity: 0.8;
  }
  .brand {
    position: absolute; left: 0; right: 0; top: 160px; text-align: center;
    font-family: "Saira", sans-serif; font-weight: 800; color: var(--paper-text);
    line-height: 1;
  }
  .brand-name { display: block; font-size: 28px; letter-spacing: 0.5px; }
  .brand-tld { display: block; font-size: 13px; margin-top: 1px; padding-left: 236px; }
  .tagline {
    position: absolute; left: 0; right: 0; top: 245px; text-align: center;
    font-family: "Saira", sans-serif; font-style: italic; font-weight: 800;
    font-size: 15px; letter-spacing: 1.4px; line-height: 20px; text-transform: uppercase;
  }
</style>
</head>
<body>
  <section class="card card-front" aria-label="Card front">
    <h1 class="holder-name">Captain Reese T. Halvorsen</h1>
    <ul class="credentials">
      <li>MRCA Licensed Master Captain</li>
      <li>CBSA Certified Instructor</li>
      <li>Graduate Degree</li>
      <li>Veteran</li>
    </ul>
    <div class="divider"></div>
    <ul class="contacts">
      <li>
        <svg viewBox="0 0 16 16" aria-hidden="true"><path fill="#111" d="M3.6 1.2l2.3 2.6-1.4 1.8c.9 2 2.5 3.6 4.4 4.5l1.8-1.4 2.6 2.3-1.3 2.4C6.8 13.6 2.5 9.2 1.2 2.6z"/></svg>
        (555) 014-2290
      </li>
      <li>
        <svg viewBox="0 0 16 16" aria-hidden="true"><rect x="1" y="3" width="14" height="10" fill="#111"/><path d="M1.5 3.5L8 9l6.5-5.5" stroke="#fff" stroke-width="1.4" fill="none"/></svg>
        service@trythelantern.com
      </li>
      <li>
        <svg viewBox="0 0 16 16" aria-hidden="true"><circle cx="8" cy="8" r="6.5" stroke="#111" stroke-width="1.6" fill="none"/><path d="M1.5 8h13M8 1.5c-3 3.5-3 9.5 0 13M8 1.5c3 3.5 3 9.5 0 13" stroke="#111" stroke-width="1.2" fill="none"/></svg>
        www.try-The-Lantern.com
      </li>
    </ul>
    <ul class="badges" aria-label="Certification badges">
      <li><span></span></li>
      <li><span></span></li>
      <li><span></span></li>
      <li><span></span></li>
    </ul>
  </section>

  <section class="card card-back" aria-label="Card back">
    <div class="boat-art" role="img" aria-label="White line illustration of a cabin motor boat"></div>
    <div class="brand">
      <span class="brand-name">TRY-THE-LANTERN</span>
      <span class="brand-tld">.COM</span>
    </div>
    <p class="tagline">Providing hands-on boat training, captaining services<br>and deliveries in the Harbor Bay County area</p>
  </section>
</body>
</html>
```